Webdesign für  Photovoltaikanlagen und E-Ladeinfrastruktur
Webdesign für Photovoltaikanlagen und E-Ladeinfrastruktur
Zielgruppe
Die VALMO Energy GmbH ist ein Spezialist für die Planung und Projektierung von Photovoltaikanlagen und E-Ladeinfrastruktur.
Aufgabenstellung
- Design-Tool: Adobe Photoshop
- Hinweis: Die Firma wird sich neue aufstellen, was das Leistungsangebot betrifft. Sie können sich deshalb nur bedingt an der derzeitigen Website orientieren, alle fremden Logos (wie z.b. ORUPA) dürfen nicht mehr genutzt werden
- Gern hätten wir einen 'frischen' Slogan im headerbild

```html
<!DOCTYPE html>
<html lang="de">
<head>
<meta charset="utf-8">
<title>VALMO Energy – Photovoltaik und E-Ladeinfrastruktur</title>
<link href="https://fonts.googleapis.com/css2?family=Montserrat:wght@400;500;600;700&display=swap" rel="stylesheet">
<style>
:root{
  --green:#00765a;
  --green-bright:#2aa84a;
  --mint:#e3f4ee;
  --ink:#111;
  --text:#222;
  --white:#fff;
}
*{margin:0;padding:0;box-sizing:border-box}
html,body{width:714px;height:1200px;overflow:hidden;background:var(--white)}
body{position:relative;font-family:'Montserrat',sans-serif;color:var(--text)}
.abs{position:absolute}
.brand{left:59px;top:24px;font-weight:700;font-size:17px;color:var(--green);letter-spacing:.5px;display:flex;align-items:center;gap:5px}
.brand .dot{width:9px;height:9px;border-radius:50%;background:var(--green)}
.contact{display:flex;align-items:center;gap:7px;font-size:6.3px;line-height:8px;top:25px}
.contact svg{width:16px;height:18px}
.nav{left:0;top:66px;width:714px;height:25px;background:var(--green)}
.nav a{position:absolute;top:7px;font-size:7.7px;font-weight:500;color:var(--white);text-decoration:none;line-height:11px}
.nav a.active{top:6px;left:58px;width:47px;height:13px;border-radius:7px;background:var(--green-bright);text-align:center;line-height:13px}
.hero{left:0;top:91px;width:714px;height:213px;background:linear-gradient(180deg,#fff 20%,#dff3ee 100%)}
.hero-photo{position:absolute;left:0;top:0;width:714px;height:213px;clip-path:polygon(337px 0,714px 0,714px 213px,252px 213px);background:linear-gradient(160deg,#7f9a6f 0%,#8aa0bf 14%,#34508f 38%,#27407c 60%,#7d8ea8 82%,#c7ced3 100%)}
.hero h1{position:absolute;left:61px;top:58px;font-size:16px;line-height:18.4px;font-weight:700;color:var(--ink)}
.hero h1 span{color:var(--green)}
.about{left:59px;top:348px;width:595px;height:199px;background:var(--white);box-shadow:0 1px 5px rgba(0,0,0,.18)}
.about h2{position:absolute;left:31px;top:33px;font-size:12px;font-weight:600;color:var(--green)}
.about p{position:absolute;left:31px;top:57px;width:242px;font-size:6.2px;line-height:13.3px}
.btn-outline{position:absolute;left:32px;top:154px;width:96px;height:17px;border:1px solid var(--green);border-radius:9px;font-size:6.3px;font-weight:600;color:var(--green);text-align:center;line-height:15px}
.about .illu{position:absolute;left:293px;top:32px;width:283px;height:138px;border-radius:6px;background:linear-gradient(180deg,#fdf0dc 0%,#f6f8f3 55%,#dcefe2 100%)}
.services{left:0;top:584px;width:714px;height:218px;background:var(--mint)}
.section-title{position:absolute;left:0;width:714px;text-align:center;font-size:12px;font-weight:600;color:var(--green)}
.card{position:absolute;top:58px;width:123px;height:130px;background:var(--white);border-radius:4px}
.card svg{position:absolute;left:31px;top:16px;width:60px;height:60px}
.card h3{position:absolute;left:0;top:86px;width:123px;text-align:center;font-size:7.5px;font-weight:600;color:var(--ink)}
.btn{position:absolute;left:13px;top:103px;width:96px;height:16px;border-radius:8px;background:var(--green);color:var(--white);font-size:6.3px;font-weight:600;text-align:center;line-height:16px}
.project-frame{left:57px;top:871px;width:259px;height:150px;background:var(--white);box-shadow:0 1px 3px rgba(0,0,0,.2)}
.project-frame .photo{position:absolute;left:4px;top:4px;width:251px;height:141px;background:linear-gradient(165deg,#9aa58a 0%,#3b5590 30%,#8c95a3 55%,#b3ad9f 75%,#7b8a5e 100%)}
.arrow{top:866px;width:14px;height:14px;border:1px solid var(--green);display:flex;align-items:center;justify-content:center}
.arrow.next{background:var(--green)}
.project h3{left:351px;top:878px;font-size:8.2px;font-weight:600;color:var(--ink)}
.project p{left:350px;top:895px;width:296px;font-size:6.3px;line-height:13.3px}
.project a{left:350px;top:948px;font-size:6.3px;color:var(--green);text-decoration:underline}
.skyline{left:0;top:1053px;width:714px;height:34px;background:linear-gradient(180deg,rgba(0,118,90,0),rgba(0,118,90,.35))}
.footer{left:0;top:1086px;width:714px;height:114px;background:var(--green);color:var(--white)}
.finfo{position:absolute;top:20px;display:flex;align-items:center;gap:7px;font-size:6.3px;line-height:8px}
.finfo b{font-weight:700}
.finfo svg{width:17px;height:18px}
.footer hr{position:absolute;left:58px;top:59px;width:596px;border:0;border-top:1px solid rgba(255,255,255,.6)}
.flinks{position:absolute;left:59px;top:70px;font-size:6.8px;font-weight:500}
.flinks span{margin:0 6px}
.copy{position:absolute;left:59px;top:85px;font-size:6.3px}
</style>
</head>
<body>
<header>
  <div class="abs brand"><span class="dot"></span>VALMO ENERGY</div>
  <div class="abs contact" style="left:275px">
    <svg viewBox="0 0 16 18" fill="none" stroke="#00765a" stroke-width="1"><path d="M8 17s-6-6-6-10a6 6 0 0 1 12 0c0 4-6 10-6 10z"/><circle cx="8" cy="7" r="2"/></svg>
    <div>Address:<br>Lindenhofweg 14, 09122 Mittelstadt</div>
  </div>
  <div class="abs contact" style="left:451px">
    <svg viewBox="0 0 18 18" fill="none" stroke="#00765a" stroke-width="1"><path d="M4 1l3 4-2 2c1 3 3 5 6 6l2-2 4 3-2 3C8 17 1 10 1 3z"/></svg>
    <div>Phone:<br>03 71 555 01-10</div>
  </div>
  <div class="abs contact" style="left:559px">
    <svg viewBox="0 0 18 14" fill="none" stroke="#00765a" stroke-width="1"><rect x="1" y="1" width="16" height="12"/><path d="M1 1l8 7 8-7"/></svg>
    <div>E-mail:<br>kontakt@valmo-energy.de</div>
  </div>
</header>
<nav class="abs nav">
  <a class="active">Home</a>
  <a style="left:136px">Unternehmen</a>
  <a style="left:234px">E-Ladeinfrastruktur</a>
  <a style="left:352px">Photovoltaik</a>
  <a style="left:442px">Planung und Projektierung</a>
  <a style="left:590px">Kontakt</a>
</nav>
<section class="abs hero">
  <div class="hero-photo" role="img" aria-label="Foto: Solarcarport über Parkplatz mit Elektroauto an der Ladesäule"></div>
  <h1>Energie von morgen –<br>heute geplant.<br><span>Sonne ernten,<br>sauber laden.</span></h1>
</section>
<section class="abs about">
  <h2>Über uns</h2>
  <p>Lorem ipsum dolor sit amet, consectetur adipiscing elit, sed do eiusmod tempor incididunt ut labore et dolore magna aliqua. Ut enim ad minim veniam, quis nostrud exercitation ullamco laboris nisi ut aliquip ex ea commodo consequat. Duis aute irure dolor in reprehenderit in voluptate velit esse cillum dolore eu fugiat nulla pariatur. Excepteur sint occaecat cupidatat non proident, sunt in culpa qui officia deserunt mollit anim id est laborum.</p>
  <div class="btn-outline">Mehr erfahren</div>
  <div class="illu" role="img" aria-label="Illustration: Stadt mit Solarmodulen, Sonne, Haus und Elektroauto"></div>
</section>
<section class="abs services">
  <h2 class="section-title" style="top:31px">Leistungen</h2>
  <div class="card" style="left:227px">
    <svg viewBox="0 0 60 60" fill="none" stroke="#00765a" stroke-width="1.6"><rect x="6" y="2" width="34" height="56" rx="5"/><rect x="12" y="8" width="22" height="8" rx="2"/><circle cx="23" cy="37" r="10"/><path d="M25 30l-5 8h5l-3 7"/><path d="M40 50h6V20h6v-6"/></svg>
    <h3>E-Ladeinfrastruktur</h3>
    <div class="btn">Mehr erfahren</div>
  </div>
  <div class="card" style="left:365px">
    <svg viewBox="0 0 60 60" fill="none" stroke="#00765a" stroke-width="1.6"><circle cx="9" cy="9" r="5"/><path d="M9 1v2M9 15v2M1 9h2M15 9h2"/><path d="M25 10h34l-12 30H13z"/><path d="M29 10l-12 30M38 10l-12 30M47 10l-12 30M21 20h34M17 30h34"/><path d="M40 40v18M30 58h20"/><rect x="2" y="46" width="20" height="12"/><path d="M22 52h18"/></svg>
    <h3>Photovoltaik</h3>
    <div class="btn">Mehr erfahren</div>
  </div>
</section>
<h2 class="section-title" style="top:837px">Planung und Projektierung</h2>
<div class="abs project-frame"><div class="photo" role="img" aria-label="Luftbild: Gewerbehallen mit Solardächern"></div></div>
<div class="abs arrow" style="left:624px"><svg width="6" height="6" viewBox="0 0 6 6" fill="none" stroke="#00765a"><path d="M4 0L1 3l3 3"/></svg></div>
<div class="abs arrow next" style="left:641px"><svg width="6" height="6" viewBox="0 0 6 6" fill="none" stroke="#fff"><path d="M2 0l3 3-3 3"/></svg></div>
<div class="project">
  <h3 class="abs">Solarstromanlagen</h3>
  <p class="abs">Lorem ipsum dolor sit amet, consectetur adipiscing elit, sed do eiusmod tempor incididunt ut labore et dolore magna aliqua. Ut enim ad minim veniam, in reprehenderit in voluptate velit esse cillum dolore.</p>
  <a class="abs">Mehr erfahren</a>
</div>
<div class="abs skyline" role="img" aria-label="Dekorative Silhouette aus Solarmodulen, Häusern, Bäumen und Windrädern"></div>
<footer class="abs footer">
  <div class="finfo" style="left:59px">
    <svg viewBox="0 0 16 18" fill="#fff"><path d="M8 18S1 10 1 7a7 7 0 0 1 14 0c0 3-7 11-7 11zm0-8a3 3 0 1 0 0-6 3 3 0 0 0 0 6z"/></svg>
    <div><b>Address:</b><br>Lindenhofweg 14, 09122 Mittelstadt</div>
  </div>
  <div class="finfo" style="left:258px">
    <svg viewBox="0 0 18 18" fill="#fff"><path d="M4 0l3 5-2 2c1 3 3 5 6 6l2-2 5 3-2 4C7 18 0 11 0 4z"/></svg>
    <div><b>Phone:</b><br>03 71 555 01-10</div>
  </div>
  <div class="finfo" style="left:404px">
    <svg viewBox="0 0 18 18" fill="#fff"><rect x="0" y="5" width="4" height="13"/><rect x="5" y="5" width="13" height="13"/><rect x="7" y="0" width="9" height="4"/></svg>
    <div><b>Fax:</b><br>03 71 555 01-199</div>
  </div>
  <div class="finfo" style="left:544px">
    <svg viewBox="0 0 18 14" fill="#fff"><path d="M0 0h18L9 7z"/><path d="M0 2l9 7 9-7v12H0z"/></svg>
    <div><b>E-mail:</b><br>kontakt@valmo-energy.de</div>
  </div>
  <hr>
  <div class="flinks">Unternehmen<span>|</span>Kontakt<span>|</span>Impressum<span>|</span>Datenschutz</div>
  <div class="copy">© 2023 valmo-energy.de</div>
</footer>
</body>
</html>
```